Bref créative
Dravel & Partners
Global Medical Device Regulatory Affairs and Quality Specialist
Professional
Merrin T. Halvorsen
President
14 Quarry Mill Road
Cicero, IN 46108
merrinhalvorsen@dravelandpart.example
www.dravelandpart.example
Please visit our website at http://dravelandpart.example/default.php# to see colors needed to be used in design.
Logo and subtitle with web address(this information should also be on the front of the card.)

```html
<!DOCTYPE html>
<html lang="en">
<head>
<meta charset="utf-8">
<title>Dravel &amp; Partners — Business Card</title>
<link href="https://fonts.googleapis.com/css2?family=Marcellus+SC&family=Tinos:ital,wght@0,400;1,400;1,700&display=swap" rel="stylesheet">
<style>
  :root {
    --backdrop: #d9d9d9;
    --card: #ffffff;
    --band: #3a2f78;
    --band-dark: #2a2160;
    --gold: #c79a2e;
    --ink: #2b2b2b;
    --purple-ink: #3a2f78;
    --mark: #5a4f98;
  }
  * { margin: 0; padding: 0; box-sizing: border-box; }
  html, body { width: 1200px; height: 780px; overflow: hidden; }
  body {
    background: var(--backdrop);
    display: flex; align-items: center; justify-content: center;
  }
  .business-card {
    position: relative;
    width: 1050px; height: 600px;
    background: var(--card);
    border-radius: 30px;
    overflow: hidden;
    box-shadow: 0 10px 30px rgba(0,0,0,.18);
  }
  .side-band {
    position: absolute; left: 0; top: 150px; bottom: 0;
    width: 205px;
    background: linear-gradient(180deg, var(--band), var(--band-dark));
  }
  .band-rule {
    position: absolute; top: 0; bottom: 0;
    width: 4px; left: 215px;
    background: var(--gold);
  }
  .band-rule.thin { left: 224px; width: 2px; background: var(--band); }
  .brand-mark {
    position: absolute; left: 50px; top: 120px;
    width: 136px; height: 136px;
    border-radius: 50%;
    background: var(--mark);
  }
  .header {
    position: absolute; left: 250px; top: 70px; right: 40px;
  }
  .company-name {
    font-family: "Marcellus SC", serif;
    font-weight: 400;
    font-size: 58px; line-height: 1;
    color: var(--ink);
    letter-spacing: 1px;
  }
  .tagline {
    margin-top: 8px;
    font-family: "Marcellus SC", serif;
    font-size: 13.5px;
    color: var(--ink);
    letter-spacing: .6px;
    white-space: nowrap;
  }
  .contact {
    position: absolute; left: 250px; top: 330px;
    font-family: "Tinos", serif;
    color: var(--ink);
  }
  .person-name {
    font-weight: 700; font-style: italic;
    font-size: 28px; line-height: 32px; color: var(--purple-ink);
  }
  .person-title {
    font-style: italic; font-size: 22px; line-height: 26px;
    color: var(--gold);
    margin-bottom: 10px;
  }
  .contact-line { font-size: 22px; line-height: 29px; white-space: nowrap; }
  .icon-column {
    position: absolute; left: 160px; top: 401px;
    display: flex; flex-direction: column; gap: 7px;
  }
  .icon-column svg { width: 22px; height: 22px; display: block; }
</style>
</head>
<body>
  <div class="business-card">
    <div class="side-band"></div>
    <div class="band-rule"></div>
    <div class="band-rule thin"></div>
    <div class="brand-mark" aria-hidden="true"></div>

    <div class="header">
      <h1 class="company-name">Dravel &amp; Partners</h1>
      <p class="tagline">Global Medical Device Regulatory Affairs &amp; Quality Specialist</p>
    </div>

    <div class="icon-column" aria-hidden="true">
      <svg viewBox="0 0 24 24"><path fill="#fff" d="M12 3 2 12h3v9h5v-6h4v6h5v-9h3z"/></svg>
      <svg viewBox="0 0 24 24"><path fill="#fff" d="M6.6 10.8a15 15 0 0 0 6.6 6.6l2.2-2.2c.3-.3.7-.4 1-.2 1.1.4 2.3.6 3.6.6.6 0 1 .4 1 1V20c0 .6-.4 1-1 1A17 17 0 0 1 3 4c0-.6.4-1 1-1h3.5c.6 0 1 .4 1 1 0 1.3.2 2.5.6 3.6.1.3 0 .7-.2 1z"/></svg>
      <svg viewBox="0 0 24 24"><path fill="#fff" d="M7 3h10v5H7zM4 9h16a1 1 0 0 1 1 1v7h-4v4H7v-4H3v-7a1 1 0 0 1 1-1zm5 7v3h6v-3z"/></svg>
      <svg viewBox="0 0 24 24"><circle cx="12" cy="12" r="9" fill="none" stroke="#fff" stroke-width="2.2"/><circle cx="12" cy="12" r="3.5" fill="none" stroke="#fff" stroke-width="2.2"/></svg>
      <svg viewBox="0 0 24 24"><circle cx="12" cy="12" r="9" fill="none" stroke="#fff" stroke-width="2"/><path d="M3 12h18M12 3c3 3 3 15 0 18M12 3c-3 3-3 15 0 18" fill="none" stroke="#fff" stroke-width="1.6"/></svg>
    </div>

    <div class="contact">
      <p class="person-name">Merrin T. Halvorsen</p>
      <p class="person-title">President</p>
      <p class="contact-line">14 Quarry Mill Road Cicero, IN 46108</p>
      <p class="contact-line">(317)555-0148</p>
      <p class="contact-line">(317)555-0193</p>
      <p class="contact-line">merrinhalvorsen@dravelandpart.example</p>
      <p class="contact-line">www.dravelandpart.example</p>
    </div>
  </div>
</body>
</html>
```